Banner Ad Design Project

We need a server banner image for our web site. The banner is to sell dedicated servers. The size needs to be 732x138 pixels.

Here is an example of the background we're thinking about: http://www.5hollowmark.com/images/banners/5hbanner.png

But feel free to be creative, and design a banner that looks good on the following page: http://www.5hollowmark.com/omnixservers.asp

Incorporate some of these words in the banner as features:
-Rapid I/O SSD Hybrid RAID
-SLA Included
-Omnix Pylo Processors
-24x7 Monitoring and Support

I like the colors on this banner... http://www.5hollowmark.com/images/banners/header-spring.png

so, maybe a white background would look good.

It Support

```html
<!DOCTYPE html>
<html lang="en">
<head>
<meta charset="utf-8">
<title>SSD Hybrid RAID Banner</title>
<link rel="stylesheet" href="https://fonts.googleapis.com/css2?family=PT+Sans+Narrow:wght@700&family=Open+Sans:wght@400&display=swap">
<style>
  :root {
    --rack-dark: #1c1a12;
    --rack-mid: #4a4432;
    --rack-light: #6b6146;
    --rack-accent: #7a2a18;
    --title-top: #fff23c;
    --title-bottom: #f2a900;
    --title-shadow: rgba(0, 0, 0, 0.85);
    --tagline: #ffffff;
  }
  html, body {
    margin: 0;
    padding: 0;
    width: 1200px;
    height: 226px;
    overflow: hidden;
    background: var(--rack-dark);
  }
  .banner {
    position: relative;
    width: 1200px;
    height: 226px;
    overflow: hidden;
  }
  .server-rack-photo {
    position: absolute;
    inset: 0;
    background:
      radial-gradient(ellipse 45% 60% at 50% 50%, rgba(20, 18, 10, 0.75), rgba(20, 18, 10, 0) 100%),
      radial-gradient(ellipse 20% 40% at 14% 40%, rgba(122, 42, 24, 0.55), rgba(122, 42, 24, 0) 100%),
      linear-gradient(90deg, var(--rack-mid) 0%, var(--rack-light) 22%, var(--rack-dark) 45%, var(--rack-mid) 70%, var(--rack-dark) 100%);
  }
  .banner-copy {
    position: absolute;
    inset: 0;
    display: flex;
    flex-direction: column;
    align-items: center;
  }
  .banner-title {
    margin: 26px 0 0;
    font-family: "PT Sans Narrow", sans-serif;
    font-weight: 700;
    font-size: 86px;
    line-height: 1;
    letter-spacing: 0.5px;
    background: linear-gradient(180deg, var(--title-top) 20%, var(--title-bottom) 95%);
    -webkit-background-clip: text;
    background-clip: text;
    color: transparent;
    filter: drop-shadow(3px 3px 3px var(--title-shadow));
  }
  .banner-tagline {
    margin: 24px 0 0;
    font-family: "Open Sans", sans-serif;
    font-weight: 400;
    font-size: 33px;
    line-height: 1;
    color: var(--tagline);
    text-shadow: 1px 1px 3px var(--title-shadow);
  }
</style>
</head>
<body>
  <div class="banner">
    <div class="server-rack-photo" role="img" aria-label="Close-up photograph of rack-mounted servers with drive bays"></div>
    <div class="banner-copy">
      <h1 class="banner-title">SSD Hybrid RAID</h1>
      <p class="banner-tagline">24x7 Monitoring and Support</p>
    </div>
  </div>
</body>
</html>
```